8 ft Straight Tension Fabric Display

Dear Valtrimonx,

We’d like you to take the above design and format it for
a narrower banner. Thanks for all your hard work. If possible, you can add another engineering image into the background, something that refers to optics or software.

Remove the wording “innovative products superlative development, high quality analytical instrumentation.”
Instead, add the following list:

Custom Development of
Instruments and Software for:

Point-of-Care Readers
Lateral Flow Strips
Fluorescence
PCR
Thermal Activation
Fluidic Control
Electrochemistry
Immunoassays

Keep the words toward the top part of the sign so that they are more at standing reader height. You can take out “QPL Harbor” and just leave the website at the bottom so there will be more room for the list.

Here are the dimensions for the banner and the instructions from Brisk Lane Signage:

33″ x 81″ Deluxe Retractable Banner

Artwork Upload Size – 33″ (Width) x 81″ (Height)

Safety Margins: (To ensure all graphic elements appear)
* Top: 1″
* Bottom: 3″

We only accept these file formats: jpg, pdf, png, ai, eps, psd
Please make sure your artwork size is the same exact size of your order. Also,do not include any bleed or crop marks.
Max File Size: 300mb

https://www.brisklanesignage.example/product/deluxe-retractable-banner-33-x-81/

Target Market(s)

technology conference

Industry/Entity Type

Medical And Science

Font styles to use
Serif
Sans Serif

Requirements
Must have
• logo
• company name, "QPL Harbor"
• phrases :
• "innovative products, superlative development"
• "high quality analytical instrumentation"
• Must match the size for the 8ft tension fabric display. Final file should be in PDF form. Single-sided display.
Nice to have
• Gold – #786D2E rgba(120, 109, 46, 1) hsla(51, 45%, 33%, 1)
• Teal- #207B75 rgba(32, 123, 117, 1) hsla(176, 59%, 30%, 1)
• Burgundy - #621515 rgba(98, 21, 21, 1) hsla(0, 65%, 23%, 1)

```html
<!DOCTYPE html>
<html lang="en">
<head>
<meta charset="utf-8">
<title>QPL Harbor – 33 x 81 Retractable Banner</title>
<link rel="stylesheet" href="https://fonts.googleapis.com/css2?family=Montserrat:wght@600;700&display=swap">
<style>
  :root {
    --burgundy: #621515;
    --burgundy-veil: rgba(120, 22, 26, 0.78);
    --brand-red: #a11d21;
    --gold: #786d2e;
    --gold-light: #c9b963;
    --teal: #207b75;
    --paper: #ffffff;
    --paper-shade: #f0f0f0;
    --stage: #e4e4e4;
    --photo-light: #e4e4e2;
    --photo-mid: #bdbdba;
    --photo-dark: #8a8a86;
  }
  * { margin: 0; padding: 0; box-sizing: border-box; }
  html, body {
    width: 1200px;
    height: 1200px;
    overflow: hidden;
    background: var(--stage);
  }
  .banner {
    position: absolute;
    left: 356px;
    top: 0;
    width: 489px;
    height: 1200px;
    overflow: hidden;
    background: var(--paper);
    font-family: "Montserrat", Arial, sans-serif;
  }
  .lab-photo {
    position: absolute;
    left: 0;
    top: 0;
    width: 489px;
    height: 700px;
    background:
      radial-gradient(ellipse at 75% 62%, var(--photo-mid) 0%, transparent 50%),
      linear-gradient(100deg, var(--photo-dark) 0%, var(--photo-mid) 45%, var(--photo-light) 80%, #d6d6d4 100%);
  }
  .optics-image {
    position: absolute;
    left: 0;
    top: 700px;
    width: 489px;
    height: 310px;
    background:
      radial-gradient(circle at 62% 48%, #d9ecea 0%, #8fbcb8 22%, transparent 48%),
      linear-gradient(160deg, #2d5b58 0%, #3f7470 45%, #9fb5b3 100%);
  }
  .veil {
    position: absolute;
    left: 0;
    top: 0;
  }
  .brand-dot {
    position: absolute;
    left: 372px;
    top: 34px;
    width: 84px;
    height: 84px;
    border-radius: 50%;
    background: var(--teal);
    border: 3px solid var(--paper);
  }
  .capabilities {
    position: absolute;
    left: 36px;
    top: 150px;
    width: 400px;
    color: var(--paper);
  }
  .capabilities-title {
    font-weight: 600;
    font-size: 24px;
    line-height: 32px;
  }
  .capabilities-rule {
    width: 90px;
    height: 4px;
    margin: 18px 0 18px;
    background: var(--gold-light);
  }
  .capabilities-list {
    list-style: none;
    font-weight: 700;
    font-size: 25px;
    line-height: 44px;
  }
  .website {
    position: absolute;
    left: 0;
    top: 1062px;
    width: 489px;
    text-align: center;
    color: var(--gold);
    font-weight: 700;
    font-size: 26px;
    letter-spacing: 0.3px;
  }
  .footer-band {
    position: absolute;
    left: 0;
    top: 1160px;
    width: 489px;
    height: 40px;
    background: var(--brand-red);
  }
</style>
</head>
<body>
<div class="banner">
  <div class="lab-photo" role="img" aria-label="Photo of a lab technician in a hairnet and white coat working at a light microscope on a bench"></div>
  <div class="optics-image" role="img" aria-label="Engineering image of an optical lens assembly beside a software analysis screen"></div>

  <svg class="veil" width="489" height="1010" viewBox="0 0 489 1010" aria-hidden="true">
    <polygon points="0,0 489,0 489,120 330,700 0,700" fill="var(--burgundy-veil)"/>
    <polygon points="0,1010 489,1010 489,1010 0,1010" fill="var(--paper-shade)"/>
  </svg>

  <div class="brand-dot" aria-hidden="true"></div>

  <section class="capabilities">
    <h1 class="capabilities-title">Custom Development<br>of Instruments and<br>Software for:</h1>
    <div class="capabilities-rule"></div>
    <ul class="capabilities-list">
      <li>Point-of-Care Readers</li>
      <li>Lateral Flow Strips</li>
      <li>Fluorescence</li>
      <li>PCR</li>
      <li>Thermal Activation</li>
      <li>Fluidic Control</li>
      <li>Electrochemistry</li>
      <li>Immunoassays</li>
    </ul>
  </section>

  <p class="website">www.qplharbor.example</p>

  <div class="footer-band"></div>
</div>
</body>
</html>
```